CANNABIS GROWING MACHINES Business Card Design

I created a front and back idea of what I want. Also I included my Brightleaf Plot logo to be used on the card. Please use your creativity to make it look professional and awesome! Use the all text and phrases in the sample card that I made.

(Front of card)Key words and phrases:
CANNABIS GROWING MACHINES
Aeroponics Technology
No soil
No pesticides
98% less water
Grow year round

(Back of card)
EVERY MONTH ONE SPIRE PLANTER WILL BE GIVEN AWAY
FOLLOW US ON IG FOR A CHANCE TO WIN A SPIRE PLANTER
CANNABIS GROWING MACHINES
Vertical Farming
Urban Farming
100% Organic
Grows 40% Faster
Indoors/outdoors

My contact info:
Chef Orv
Phone:415 730-2184
web: brightleafplot.example
IG: leafyrootriders

Target Market(s)

Cannabis Cultivation, Gardening, Urban farming, Vertical farming

Industry/Entity Type

Cannabis

Contact Information for Business Card

My contact info:
Chef Orv
Phone:415 730-2184
web: brightleafplot.example
IG: leafyrootriders

Requirements
Must have
• My contact info:
Chef Orv
Phone:415 730-2184
web: brightleafplot.example
IG: leafyrootriders
Nice to have
• Awesome Cannabis imagery throughout the card front and back.

```html
<!DOCTYPE html>
<html lang="en">
<head>
<meta charset="utf-8">
<title>Brightleaf Plot – Business Card</title>
<link href="https://fonts.googleapis.com/css2?family=Tenor+Sans&display=swap" rel="stylesheet">
<style>
  :root {
    --backdrop: #2b2b2b;
    --card: #fbfbf9;
    --leaf-green: #7dbb2e;
    --ink: #3d3d3d;
    --ink-soft: #5a5a5a;
    --band: #f2f2f2;
    --photo-light: #a7b48f;
    --photo-mid: #6f7f56;
    --photo-dark: #3f4a30;
    --white: #ffffff;
  }
  * { margin: 0; padding: 0; box-sizing: border-box; }
  html, body {
    width: 1200px; height: 900px; overflow: hidden;
    background: var(--backdrop);
    font-family: "Tenor Sans", "Gill Sans", sans-serif;
  }
  .sheet {
    width: 1200px; height: 900px;
    display: flex; flex-direction: column; align-items: center; justify-content: center; gap: 24px;
  }
  .card {
    width: 700px; height: 400px; position: relative; overflow: hidden;
    background: var(--card);
    box-shadow: 0 10px 30px rgba(0,0,0,.45);
  }

  /* Contact side */
  .contact-side { text-align: center; padding-top: 30px; }
  .contact-name { color: var(--leaf-green); font-size: 30px; letter-spacing: 1px; }
  .contact-row {
    margin-top: 10px; display: flex; justify-content: center; align-items: center; gap: 22px;
    color: var(--ink-soft); font-size: 17px;
  }
  .contact-item { display: flex; align-items: center; gap: 7px; }
  .contact-item svg { width: 16px; height: 16px; }
  .ig-dot { width: 14px; height: 14px; border-radius: 50%; background: var(--leaf-green); }
  .divider {
    display: flex; align-items: center; justify-content: center; gap: 14px;
    margin: 14px auto; width: 440px;
  }
  .divider-line { flex: 1; height: 2px; background: var(--leaf-green); }
  .divider-mark { width: 16px; height: 16px; border-radius: 50%; background: var(--leaf-green); }
  .giveaway { color: var(--ink); font-size: 19px; line-height: 1.35; letter-spacing: .5px; }
  .features { color: var(--ink-soft); font-size: 17px; line-height: 1.35; }

  /* Brand side */
  .brand-band {
    position: absolute; inset: 0 0 auto 0; height: 180px; background: var(--band);
    text-align: center; padding-top: 26px;
  }
  .brand-name {
    display: flex; align-items: center; justify-content: center; gap: 14px;
    color: var(--ink); font-size: 34px; letter-spacing: 6px;
  }
  .brand-dot { width: 26px; height: 26px; border-radius: 50%; background: var(--leaf-green); }
  .brand-tagline { margin-top: 16px; color: var(--leaf-green); font-size: 27px; letter-spacing: .5px; }
  .brand-tech { color: var(--leaf-green); font-size: 23px; margin-top: 2px; }
  .grow-photo {
    position: absolute; inset: 180px 0 0 0;
    background: linear-gradient(160deg, var(--photo-light) 0%, var(--photo-mid) 45%, var(--photo-dark) 100%);
  }
  .benefits {
    position: absolute; left: 230px; top: 200px;
    color: var(--white); font-size: 30px; line-height: 1.3; list-style: none;
    text-shadow: 0 1px 3px rgba(0,0,0,.4);
  }
</style>
</head>
<body>
<main class="sheet">

  <section class="card contact-side">
    <h1 class="contact-name">CHEF ORV</h1>
    <div class="contact-row">
      <span class="contact-item">
        <svg viewBox="0 0 16 16" aria-hidden="true"><path d="M3 2h3l1.5 3.5-2 1.3a9 9 0 0 0 3.7 3.7l1.3-2L14 10v3a1 1 0 0 1-1 1A11 11 0 0 1 2 3a1 1 0 0 1 1-1z" fill="#7dbb2e"/></svg>
        415 730-2184
      </span>
      <span class="contact-item">
        <svg viewBox="0 0 16 16" aria-hidden="true"><circle cx="8" cy="8" r="6.5" fill="none" stroke="#7dbb2e" stroke-width="1.6"/><path d="M1.5 8h13M8 1.5c-3 3.5-3 9.5 0 13M8 1.5c3 3.5 3 9.5 0 13" fill="none" stroke="#7dbb2e" stroke-width="1.2"/></svg>
        brightleafplot.example
      </span>
      <span class="contact-item"><span class="ig-dot"></span>leafyrootriders</span>
    </div>

    <div class="divider"><span class="divider-line"></span><span class="divider-mark" role="img" aria-label="small leaf emblem"></span><span class="divider-line"></span></div>

    <p class="giveaway">EVERY MONTH ONE SPIRE PLANTER WILL BE GIVEN AWAY<br>FOLLOW US ON IG FOR A CHANCE TO WIN A SPIRE PLANTER<br>CANNABIS GROWING MACHINES</p>

    <div class="divider"><span class="divider-line"></span><span class="divider-mark" role="img" aria-label="small leaf emblem"></span><span class="divider-line"></span></div>

    <p class="features">Vertical Farming / Urban Farming<br>100% Organic / Grows 40% Faster<br>Indoors / outdoors</p>
  </section>

  <section class="card brand-side">
    <div class="grow-photo" role="img" aria-label="Photo of a dense field of flowering cannabis plants"></div>
    <header class="brand-band">
      <div class="brand-name"><span class="brand-dot"></span>BRIGHTLEAF PLOT</div>
      <p class="brand-tagline">CANNABIS GROWING MACHINES</p>
      <p class="brand-tech">Aeroponics Technology</p>
    </header>
    <ul class="benefits">
      <li>No soil</li>
      <li>No pesticides</li>
      <li>98% less water</li>
      <li>Grow year round</li>
    </ul>
  </section>

</main>
</body>
</html>
```